Nutrition business needs logo & business card design

We need a business card & logo design for a new company based in Toronto, Ontario Canada called Verdel Wellworks.

We provide nutrition service using metrics as guide to manage client's progress. Our service creates individualized nutrition and lifestyle strategies that focuses on improving Performance, Longevity and Weight Loss. I would like to see designs that use the color of green, gray, blue and white.

The final design should:

--convey a feeling of connectedness with positive transformation.

-- communicate the idea of awareness with guided effort that yields personal independence for a better and more productive life

Target Market(s)

Professionals who work in the IT/Computer/Engineering/Banking industry specifically Directors, Managers, CEO's.

Industry/Entity Type

Health And Wellness

Contact Information for Business Card

Dorvany Pask, Owner
email: DPASK@verdelwellworks.example
tel: - 416-555-0148

Logo Text

better health through analytics or measure to manage

Font styles to use
Other font styles liked:
• Garamound

Colors
ffffff
abd037
85acd3
757575
34a7d7

Requirements
Must have
• Good contrast and decent size font - ease of readability, aesthetically nice colors
Nice to have
• image of chart or graph that conveys measurement or analytics
Should not have
• Borders, images of food,

```html
<!DOCTYPE html>
<html lang="en">
<head>
<meta charset="utf-8">
<title>Verdel Wellworks – Business Cards</title>
<link rel="stylesheet" href="https://fonts.googleapis.com/css2?family=Barlow:wght@500;600&family=EB+Garamond:wght@700&display=swap">
<style>
  :root {
    --stage: #1f242b;
    --card: #ffffff;
    --blue: #2fa6d6;
    --green: #07a94c;
    --gray: #4a4a4c;
    --gray-soft: #66676a;
  }
  * { box-sizing: border-box; margin: 0; padding: 0; }
  html, body { width: 1200px; height: 1200px; overflow: hidden; }
  body { background: var(--stage); position: relative; font-family: "Barlow", sans-serif; }

  .card {
    position: absolute; left: 234px; width: 686px; height: 380px;
    background: var(--card); border-radius: 32px; overflow: hidden;
  }
  .card--front { top: 138px; }
  .card--alt { top: 612px; }

  .strip-tab { position: absolute; left: 377px; top: 0; width: 43px; height: 12px; background: var(--blue); }
  .icon-box {
    position: absolute; left: 377px; width: 43px; height: 43px; background: var(--blue);
    display: flex; align-items: center; justify-content: center;
  }
  .icon-box--pin { top: 171px; }
  .icon-box--phone { top: 219px; }
  .icon-box--mail { top: 268px; height: 112px; align-items: flex-start; padding-top: 8px; }
  .icon-box svg { width: 22px; height: 22px; fill: #fff; }
  .at { color: #fff; font-family: "Barlow", sans-serif; font-size: 25px; font-weight: 600; line-height: 1; }

  .holder-name {
    position: absolute; left: 379px; top: 50px; font-size: 42px; font-weight: 600;
    color: var(--blue); line-height: 1; letter-spacing: 0.5px;
  }
  .holder-role {
    position: absolute; left: 379px; top: 104px; font-size: 28px; font-weight: 500;
    color: var(--gray-soft); line-height: 1; letter-spacing: 0.5px;
  }
  .contact {
    position: absolute; left: 434px; font-family: "EB Garamond", serif; font-weight: 700;
    font-size: 15px; color: var(--gray-soft); line-height: 1; white-space: nowrap;
  }
  .card--alt .contact { color: var(--blue); }
  .contact--address { top: 187px; }
  .contact--phone { top: 233px; }
  .contact--email { top: 281px; }

  .brand { position: absolute; display: flex; align-items: center; }
  .brand--front { left: 54px; top: 158px; gap: 14px; }
  .brand--front .brand-name {
    font-size: 50px; font-weight: 600; color: var(--gray); line-height: 0.98; letter-spacing: 0.5px;
  }
  .brand--front .brand-dot { width: 30px; height: 30px; border-radius: 50%; background: var(--blue); }
  .brand--alt { left: 60px; top: 108px; flex-direction: column; align-items: center; gap: 26px; width: 190px; }
  .brand--alt .brand-mark { width: 118px; height: 118px; background: var(--green); }
  .brand--alt .brand-name {
    font-size: 25px; font-weight: 500; color: var(--gray); line-height: 1; letter-spacing: 0.5px; white-space: nowrap;
  }
</style>
</head>
<body>

<section class="card card--front">
  <div class="brand brand--front">
    <div class="brand-name">Verdel<br>Wellworks</div>
    <span class="brand-dot"></span>
  </div>
  <span class="strip-tab"></span>
  <h1 class="holder-name">Dorvany Pask</h1>
  <p class="holder-role">Owner</p>
  <div class="icon-box icon-box--pin">
    <svg viewBox="0 0 24 24"><path d="M12 1a7.5 7.5 0 0 0-7.5 7.5C4.5 14 12 23 12 23s7.5-9 7.5-14.5A7.5 7.5 0 0 0 12 1zm0 10.5a3 3 0 1 1 0-6 3 3 0 0 1 0 6z"/></svg>
  </div>
  <div class="icon-box icon-box--phone">
    <svg viewBox="0 0 24 24"><path d="M7 2l3 1-1 6-2 1c0 3 2 7 4 9l2-1 4 4-2 2c-5 0-12-9-12-16l4-6z"/></svg>
  </div>
  <div class="icon-box icon-box--mail"><span class="at">@</span></div>
  <p class="contact contact--address">#00 Adress 01, Adress, City</p>
  <p class="contact contact--phone">416-555-0148</p>
  <p class="contact contact--email">DPASK@verdelwellworks.example</p>
</section>

<section class="card card--alt">
  <div class="brand brand--alt">
    <span class="brand-mark"></span>
    <div class="brand-name">Verdel Wellworks</div>
  </div>
  <span class="strip-tab"></span>
  <h2 class="holder-name">Dorvany Pask</h2>
  <p class="holder-role">Owner</p>
  <div class="icon-box icon-box--pin">
    <svg viewBox="0 0 24 24"><path d="M12 1a7.5 7.5 0 0 0-7.5 7.5C4.5 14 12 23 12 23s7.5-9 7.5-14.5A7.5 7.5 0 0 0 12 1zm0 10.5a3 3 0 1 1 0-6 3 3 0 0 1 0 6z"/></svg>
  </div>
  <div class="icon-box icon-box--phone">
    <svg viewBox="0 0 24 24"><path d="M7 2l3 1-1 6-2 1c0 3 2 7 4 9l2-1 4 4-2 2c-5 0-12-9-12-16l4-6z"/></svg>
  </div>
  <div class="icon-box icon-box--mail"><span class="at">@</span></div>
  <p class="contact contact--address">#00 Adress 01, Adress, City</p>
  <p class="contact contact--phone">416-555-0148</p>
  <p class="contact contact--email">DPASK@verdelwellworks.example</p>
</section>

</body>
</html>
```